Update of Personal Website: geraldwinthorpe.com

This is a revamp of a personal website that already exists. Please visit the URL in the project title to view the current site.

An entirely fresh look is needed for the new site. Edits need to be made to the text included on the current site and photos must be added and subtracted. I will provide this.

Once a designer is selected, details about the necessities of the project will be discussed.

Target Market(s)

Business professionals

Industry/Entity Type

Real Estate Development

Coding

Coded - Design and coding required

Number of Pages Required

5+ page

Font styles to use
Sans Serif

Colors

Designer to choose colors to be used in the design.

Requirements
Must have
• Clean home page. Light background. Simplistic nature.
• Pages: Home, Family, Community, Business
Nice to have
• See attached images for examples of attractive sites.

```html
<!DOCTYPE html>
<html lang="en">
<head>
<meta charset="utf-8">
<title>Gerald Winthorpe</title>
<link rel="stylesheet" href="https://fonts.googleapis.com/css2?family=Raleway:ital,wght@0,400;0,500;0,600;0,700;0,800;1,400;1,500&display=swap">
<style>
  :root {
    --accent: #1aa3e8;
    --ink: #111111;
    --text: #333333;
    --hero-light: #ffffff;
    --hero-dark: #e4e4e4;
    --footer: #333333;
    --footer-text: #dddddd;
    --white: #ffffff;
  }
  * { margin: 0; padding: 0; box-sizing: border-box; }
  html, body { width: 1200px; height: 836px; overflow: hidden; background: var(--white); }
  body { font-family: "Raleway", Arial, sans-serif; color: var(--text); position: relative; }

  .site-nav { position: absolute; top: 0; left: 0; width: 1200px; height: 62px; background: var(--white); }
  .site-nav ul { list-style: none; display: flex; justify-content: center; gap: 0; padding-left: 18px; }
  .site-nav li { position: relative; padding: 0 17px; line-height: 62px; font-size: 12px; font-weight: 700; color: var(--ink); letter-spacing: 0.2px; }
  .site-nav li.is-active { color: var(--accent); }
  .site-nav li.is-active::before { content: ""; position: absolute; top: 0; left: 0; right: 0; height: 4px; background: var(--accent); }

  .hero { position: absolute; top: 62px; left: 0; width: 1200px; height: 478px;
    background: radial-gradient(ellipse at 62% 30%, var(--hero-light) 0%, #f3f3f3 45%, var(--hero-dark) 100%); overflow: hidden; }
  .hero-portrait { position: absolute; left: 730px; top: 12px; width: 360px; height: 466px;
    background: linear-gradient(180deg, #c9b7a6 0%, #8a8a8f 35%, #6e6e74 70%, #5b5b60 100%);
    border-radius: 160px 160px 0 0; }
  .hero-copy { position: absolute; left: 121px; top: 48px; width: 600px; }
  .hero-name { font-weight: 800; line-height: 0.9; letter-spacing: -1px; }
  .hero-name .first { display: block; font-size: 74px; background: linear-gradient(180deg, #777 0%, #333 100%);
    -webkit-background-clip: text; background-clip: text; color: transparent; }
  .hero-name .last { display: block; font-size: 82px; color: var(--ink); }
  .hero-lead { margin-top: 14px; font-style: italic; font-size: 17px; line-height: 25px; color: #222; font-weight: 500; }
  .hero-body { margin-top: 14px; font-size: 12.5px; line-height: 20.3px; color: #333; }
  .connect { margin-top: 20px; display: flex; align-items: center; gap: 14px; }
  .connect-label { font-size: 16px; font-weight: 700; color: var(--ink); margin-right: 2px; }
  .connect-dot { width: 16px; height: 16px; border-radius: 50%; background: var(--accent); }

  .slide-arrow { position: absolute; top: 238px; width: 20px; height: 34px; }
  .slide-arrow.prev { left: 57px; }
  .slide-arrow.next { left: 1121px; }

  .feature-tiles { position: absolute; top: 545px; left: 0; width: 1200px; height: 193px; }
  .tile { position: absolute; top: 0; height: 193px; overflow: hidden; background: #000; color: var(--white); }
  .tile-photo { position: absolute; top: 0; right: 0; height: 100%; }
  .tile-family { left: 0; width: 399px; }
  .tile-family .tile-photo { width: 235px; background: linear-gradient(90deg, #000 0%, #5a4a40 35%, #b29a86 70%, #d8c7b8 100%); }
  .tile-community { left: 402px; width: 397px; }
  .tile-community .tile-photo { width: 300px; background: linear-gradient(90deg, #000 0%, #3a2a22 40%, #8a6650 75%, #4a3a34 100%); }
  .tile-business { left: 802px; width: 398px; }
  .tile-business .tile-photo { width: 300px; background: linear-gradient(90deg, #000 0%, #2a3e6a 35%, #b59a5a 70%, #3d5ea6 100%); }
  .tile-content { position: absolute; left: 30px; top: 60px; }
  .tile-family .tile-content { left: 76px; }
  .tile-business .tile-content { left: 30px; }
  .tile-title { font-size: 31px; font-weight: 700; line-height: 1; letter-spacing: 0.3px; }
  .tile-text { margin-top: 11px; font-size: 15px; line-height: 21px; width: 200px; }
  .tile-link { display: block; margin-top: 10px; font-size: 11px; font-weight: 700; color: var(--accent); letter-spacing: 0.3px; }

  .site-footer { position: absolute; top: 742px; left: 0; width: 1200px; height: 94px; background: var(--footer); }
  .copyright { position: absolute; left: 76px; top: 39px; font-size: 12px; color: var(--footer-text); }
  .footer-nav { position: absolute; right: 75px; top: 40px; list-style: none; display: flex; gap: 32px; }
  .footer-nav li { font-size: 11px; font-weight: 700; color: var(--footer-text); }
</style>
</head>
<body>
  <nav class="site-nav">
    <ul>
      <li class="is-active">HOME</li>
      <li>FAMILY</li>
      <li>COMMUNITY</li>
      <li>BUSINESS</li>
      <li>CONTACT</li>
    </ul>
  </nav>

  <section class="hero">
    <div class="hero-portrait" role="img" aria-label="Portrait of Gerald Winthorpe in a grey pinstripe suit and orange tie"></div>
    <div class="hero-copy">
      <h1 class="hero-name"><span class="first">GERALD</span><span class="last">WINTHORPE</span></h1>
      <p class="hero-lead">Gerald Winthorpe completed his first real estate transaction at the age of 19. He is now one of the most recognized contributors to the real estate industry in the Southern United States.</p>
      <p class="hero-body">Winthorpe is the driving force behind the upscale residential and mixed-use communities of Winthorpe Development &amp; Realty LLC (WDR) and his most recent venture with Winthorpe-Halvorsen. Under his guidance, both brands set the standard for quality and consistency. While remaining committed to the centralized multifamily niche, his broad real estate portfolio includes office, institutional, recreational, and industrial applications.</p>
      <div class="connect">
        <span class="connect-label">CONNECT:</span>
        <span class="connect-dot" aria-label="Social profile"></span>
        <span class="connect-dot" aria-label="Social profile"></span>
        <span class="connect-dot" aria-label="Social profile"></span>
        <span class="connect-dot" aria-label="Social profile"></span>
        <span class="connect-dot" aria-label="Social profile"></span>
      </div>
    </div>
    <svg class="slide-arrow prev" viewBox="0 0 20 34" aria-label="Previous slide"><path d="M16 3 L4 17 L16 31" fill="none" stroke="#999" stroke-width="4" stroke-linecap="round" stroke-linejoin="round"/></svg>
    <svg class="slide-arrow next" viewBox="0 0 20 34" aria-label="Next slide"><path d="M4 3 L16 17 L4 31" fill="none" stroke="#999" stroke-width="4" stroke-linecap="round" stroke-linejoin="round"/></svg>
  </section>

  <section class="feature-tiles">
    <article class="tile tile-family">
      <div class="tile-photo" role="img" aria-label="Family photo of Gerald Winthorpe with his wife and children"></div>
      <div class="tile-content">
        <h2 class="tile-title">FAMILY</h2>
        <p class="tile-text">Devoted husband and father of five...</p>
        <span class="tile-link">LEARN MORE &raquo;</span>
      </div>
    </article>
    <article class="tile tile-community">
      <div class="tile-photo" role="img" aria-label="Gerald Winthorpe at a community evening event"></div>
      <div class="tile-content">
        <h2 class="tile-title">COMMUNITY</h2>
        <p class="tile-text">Committed to the community...</p>
        <span class="tile-link">LEARN MORE &raquo;</span>
      </div>
    </article>
    <article class="tile tile-business">
      <div class="tile-photo" role="img" aria-label="Multifamily apartment building at dusk"></div>
      <div class="tile-content">
        <h2 class="tile-title">BUSINESS</h2>
        <p class="tile-text">Leading the Multi-family Development industry...</p>
        <span class="tile-link">LEARN MORE &raquo;</span>
      </div>
    </article>
  </section>

  <footer class="site-footer">
    <p class="copyright">Copyright &copy; 2017 Gerald Winthorpe. All Rights Reserved</p>
    <ul class="footer-nav">
      <li>HOME</li>
      <li>FAMILY</li>
      <li>COMMUNITY</li>
      <li>BUSINESS</li>
      <li>CONTACT</li>
    </ul>
  </footer>
</body>
</html>
```